Brochure Design Project A5 (UK) 64 pages apox Making Money From Financial Trading

I require a website (long sales letter) turned into a A5 booklet for mailing out will will be full colour. You must provide a complete end to end to service, I will provide all the text and photos and you need to layout and design the brochure, resize photos to fit. I see the size being around 64 sides of UK A5 paper
148 x 210mm 5.83 x 8.27

You must be creative with text layout and typography, this is very text heavy over 10,000 words in to total. the website can be seen at www.brassfold-ledger.com however this is NOT the final text but gives you an idea. (I have attached 5 pages of text)

They typical reader is male over 40, it needs to be readable, experience with magazine layouts and advantage

The finished project must be ready to go to print.

So it needs a front and back cover designed - I have attached a sample DVD cover as an idea from one of our products and then the inside pages, designed/set out
Updates

We have made the project guaranteed so step up and give me your best designs

Reason: Dear All. The standard of work submitted so far has been very poor and amateurish. We have decided to use another company for the front and back cover, therefore leaving you to concentrate on the text for inside the booklet. If you wish to resubmit some better designs then please go ahead. Thx

Target Market(s)

The typical client is Male, professional, looking make money from the stockmarket. The end user already knows the author

Industry/Entity Type

Financial

Requirements
Must have
• Must have good and creative typography

```html
<!DOCTYPE html>
<html lang="en">
<head>
<meta charset="utf-8">
<title>Private Mentor – Spread</title>
<link rel="stylesheet" href="https://fonts.googleapis.com/css2?family=Alegreya+Sans:wght@400;500;700&display=swap">
<style>
  :root{
    --ink:#2b2b2b;
    --orange:#cf5f12;
    --navy:#1e4e86;
    --green:#2e7b16;
    --band:#0b0b0b;
    --sky-top:#eef4fa;
    --sky-bottom:#dbe7f2;
  }
  *{box-sizing:border-box;margin:0;padding:0}
  html,body{width:1200px;height:846px;overflow:hidden}
  body{font-family:"Alegreya Sans",sans-serif;color:var(--ink);background:#fff}
  .spread{position:relative;width:1200px;height:846px;overflow:hidden;
    background:linear-gradient(180deg,var(--sky-top) 0%,#f4f8fc 35%,var(--sky-bottom) 100%)}
  .crowd{position:absolute;left:0;top:470px;width:1200px;height:362px;
    background:linear-gradient(180deg,rgba(150,170,195,0) 0%,rgba(150,170,195,.22) 60%,rgba(150,170,195,.3) 100%)}
  .band{position:absolute;left:0;width:1200px;background:var(--band)}
  .band--top{top:0;height:13px}
  .band--bottom{top:832px;height:14px}
  .block{position:absolute;font-size:15.5px;line-height:24.2px}
  .ln{display:block;white-space:nowrap}
  .ln.j{text-align:justify;text-align-last:justify}
  .heading{position:absolute;color:var(--orange);font-weight:500;font-size:18.5px;line-height:24px;white-space:nowrap}
  .portrait{position:absolute;left:19px;top:56px;width:174px;height:222px;border:3px solid #fff;
    box-shadow:0 0 0 1px #c9d3dd;background:linear-gradient(160deg,#8b8f92 0%,#7c8aa8 45%,#5d6e9a 100%)}
  .byline{position:absolute;left:197px;top:161px;width:460px;color:var(--navy);font-weight:500;font-size:18.5px;line-height:24.5px}
  .pull-quote{position:absolute;left:22px;top:414px;width:636px;text-align:center;color:var(--green);
    font-weight:500;font-size:20px;line-height:24px}
  .strong{font-weight:700;color:#1a1a1a}
  .product{position:absolute;left:0;top:0;width:1200px;height:846px;
    clip-path:polygon(985px 632px,1200px 662px,1200px 832px,768px 832px,792px 736px,952px 722px);
    background:linear-gradient(120deg,#2a2a2a 0%,#4a4a4a 30%,#1c1c1c 60%,#3b4b63 100%)}
</style>
</head>
<body>
<main class="spread">
  <div class="crowd" role="img" aria-label="Faint silhouettes of a crowd of business people"></div>
  <div class="band band--top"></div>

  <h2 class="heading" style="left:22px;top:24px">And here is what Hal Brennick said:</h2>
  <div class="portrait" role="img" aria-label="Portrait photograph of Hal Brennick"></div>

  <p class="block" style="left:201px;top:54px;width:446px">
    <span class="ln j">“I cannot do what Milo does; he is a shorter term trader, I am a longer</span>
    <span class="ln j">term person. But if you combine what he does and I do then my goodness,</span>
    <span class="ln j">you will become extremely successful and one day we will come and</span>
    <span class="ln">work for you”</span>
  </p>
  <p class="byline">Hal Brennick co funder of Meridian Fund with Edwin Marlow and Brennick Raw Materials Index.</p>
  <p class="block" style="left:197px;top:223px;width:446px">
    <span class="ln j">By the way, you don’t have to be based in the UK to do this (I am not) and</span>
    <span class="ln j">although I have stated my earnings in Pounds, you can easily be earning</span>
    <span class="ln j">the same in Euros, US$, Australian Dollars, Swiss Francs, South African</span>
    <span class="ln">Rand or any major currency.</span>
  </p>
  <p class="block" style="left:26px;top:331px;width:624px">
    <span class="ln j">And the real beauty of what I’m going to show you today is that you can continue to make thousands a</span>
    <span class="ln">week wherever you are in the world.</span>
    <span class="ln">But before we go further let me ask you a question.</span>
  </p>

  <blockquote class="pull-quote">
    <span class="ln">“Do you think it would be easier for you to reach your financial goals if you</span>
    <span class="ln">had a personal mentor? Someone who had amassed a multi-million pound</span>
    <span class="ln">fortune, starting with nothing and who was prepared to stand by your side</span>
    <span class="ln">until YOU achieved your goals as well?”</span>
  </blockquote>

  <p class="block" style="left:26px;top:518px;width:624px">
    <span class="ln">Imagine – you could ask that person ANY question you liked – and they would tell you the real,</span>
    <span class="ln">bottom line truth.</span>
    <span class="ln">If you were struggling, they’d be there with their years of wisdom, experience and raw money-making</span>
    <span class="ln">know-how to show you the way.</span>
    <span class="ln">If you were lost or confused, like a close friend, your mentor would be by your side to set you straight.</span>
    <span class="ln">Yes, there are books, manuals and DVDs a-plenty. But after you’ve handed over your cash to the</span>
    <span class="ln">gurus selling their wares – all offering to teach you how to get rich – are the authors around to answer</span>
    <span class="ln">tricky questions? Or have they long vanished?</span>
    <span class="ln">I think you know the answer...</span>
    <span class="ln">The harsh truth is that virtually nobody who has made serious money is willing to make themselves</span>
    <span class="ln">available to those who are just starting on the first rung of the ladder.</span>
    <span class="ln">Until now.</span>
  </p>

  <p class="block" style="left:675px;top:50px;width:500px">
    <span class="ln">For the last 3 years, I have mentored my members personally, sharing my own</span>
    <span class="ln">trades and investments, explaining my techniques and answering questions and</span>
    <span class="ln">emails personally. Every member has my personal email details. My members also</span>
    <span class="ln">get access to my 26 years of contacts which span the globe and are able to see my</span>
    <span class="ln">own trades.</span>
  </p>
  <h2 class="heading" style="left:675px;top:183px">The secrets of making money in financial markets</h2>
  <div class="block" style="left:675px;top:213px;width:505px">
    <p>
      <span class="ln">Many try to complicate this business; they like to use jargon or appear important. I</span>
      <span class="ln">am sure you have seen these “gurus” on business channels, but the truth is, most of</span>
      <span class="ln">them don’t have a pot to piss in. The may manage billions of other people’s money,</span>
      <span class="ln">but they have no skin in the game.</span>
    </p>
    <p style="margin-top:24px">
      <span class="ln">I don’t take a penny of investment capital from anyone else, I genuinely trade and</span>
      <span class="ln">invest my own account(s) and I “eat my own cooking”.</span>
    </p>
    <p style="margin-top:24px">
      <span class="ln">Would you like to be my Private Student for the next 12 months and trade alongside</span>
      <span class="ln">me from the comfort of your home? Would you like me to show you how to earn a</span>
      <span class="ln">very large <span class="strong">INCOME</span> from Financial Trading and trading other financial products</span>
      <span class="ln">using this system ... a system which I’ve used and perfected over the last ten years</span>
      <span class="ln">and which I’ve personally used to average over £24,900 PER WEEK?</span>
    </p>
    <p style="margin-top:24px">
      <span class="ln">Would you like me to be your Personal Mentor? If you do, you’ll need access to the</span>
      <span class="ln">Internet ... and about <span class="strong">20-30 minutes spare each day</span> to follow some simple steps.</span>
      <span class="ln">And don’t worry if you know little or nothing about Internet Financial Trading.</span>
      <span class="ln">You’ll need absolutely...</span>
      <span class="ln">NO Experience</span>
      <span class="ln strong">How would you like THIS job description?</span>
      <span class="ln">No Job (that’s a great Job description in itself)</span>
    </p>
  </div>

  <div class="product" role="img" aria-label="Home study course pack with printed cover and two DVD discs"></div>

  <div class="band band--bottom"></div>
</main>
</body>
</html>
```